Kora_Plastering Web Design Project

Kora Plastering wants a modern looking 1 page website that clearly emphasises the 3 specialised construction services:
1. Plastering = (inside walls etc)
2. Rendering = (outside walls etc)
3. Cornicing = (inside wall and ceilings)

Kora Plastering is run by craftsmen, so be creative.

I really like http://quillnorth-example.com

The site design lends itself well to being a one pager - I like the html click thru panel (at the base above the fold) that allows reader to stay on the one page but can see see more info by tapping on the red arrows.

The site is also successful because it doesn't rely on photos - but makes the most of big headlines and client testimonials.

I could provide you with more content if you need it to achieve this kind of site.

Project Deadline Extended
Reason: Hi, we have decided to extend the deadline as we have only received ideas from one designer. We feel there is still scope to improve on the designs we have received so far. Improvements in the following areas: - design that complements the new logo design (the logo shows that KORA provide services inside and outside the house) - the design doesn't look like one of the many 'template' designs you see these days - the design does not need to use photos - if you can illustrate well as well as design website you will have an advantage! - site should look very modern / up to date We have now guaranteed payment in case designers were holding off.

Target Market(s)

Architects, interior designers, builders, home owners

Industry/Entity Type

Construction

Requirements
Must have
• Design at 1024 x 768
Website design should complement new logo - with black and ivory being dominant colours. (Logo is attached)
The site should be creative - as creativity is one of the key aspects of the service provide by Kora Plastering.
Text for the site has been provided - see pdf
Nice to have
• It's not essential to use photos. In the quick example I have attached I have sourced photos from snapverde-example.com
File #: 8302947 / File #: 40918526 / File #: 9175382. I repeat photos are not mandatory - you may prefer to use other graphical devices.
Easily coded
Modern looking design

```html
<!DOCTYPE html>
<html lang="en">
<head>
<meta charset="utf-8">
<title>Kora Plastering</title>
<link rel="stylesheet" href="https://fonts.googleapis.com/css2?family=Archivo:wght@800&family=Lato:wght@400&family=PT+Serif&family=Rokkitt:wght@700&display=swap">
<style>
:root{
  --black:#000;
  --ink:#1d1a16;
  --ivory:#f3e8cf;
  --ivory-light:#faf4e4;
  --gold:#f2a51c;
  --gold-line:#a8864a;
  --footer-yellow:#f3e27a;
  --grey-text:#7a7a7a;
  --card-border:#d8d8d8;
  --rule:#9a9a9a;
}
*{margin:0;padding:0;box-sizing:border-box}
html,body{width:1169px;height:1200px;overflow:hidden;background:#fff}
body{position:relative;font-family:"PT Serif",Georgia,serif;color:var(--ink)}

.topbar{position:absolute;left:0;top:0;width:1169px;height:65px;background:var(--black)}
.topbar-name{position:absolute;left:30px;top:14px;color:#fff;font-family:"Rokkitt",serif;font-weight:700;font-size:22px;line-height:18px;letter-spacing:1px}
.topbar-name span{display:block;font-size:13px;letter-spacing:3px}
.main-nav{position:absolute;right:30px;top:0;height:65px;display:flex}
.main-nav a{color:#fff;text-decoration:none;font-family:"Lato",sans-serif;font-size:19px;line-height:61px;padding:0 18px;border-left:1px solid #333}
.main-nav a:first-child{border-left:none}

.hero{position:absolute;left:0;top:65px;width:1169px;height:283px;background:radial-gradient(ellipse at 40% 50%,var(--ivory-light),var(--ivory) 75%,#e9dcbc);border-bottom:3px solid var(--gold-line)}
.hero-name{position:absolute;left:22px;top:72px;font-family:"Rokkitt",serif;font-weight:700;color:#231f1c;font-size:96px;line-height:80px;letter-spacing:4px}
.hero-name span{display:block;font-size:37px;line-height:40px;letter-spacing:11px}
.hero-headline{position:absolute;right:34px;top:110px;text-align:right;font-family:"Archivo",sans-serif;font-weight:800;font-size:43px;line-height:48px;letter-spacing:-2px;color:#1c1a18}
.hero-cta{position:absolute;left:852px;top:221px;width:283px;height:46px;border-radius:8px;border:1px solid #d9c892;background:linear-gradient(#fffbe0,#f7e39a 60%,#efd36e);font-family:"Archivo",sans-serif;font-weight:800;font-size:24px;letter-spacing:-1px;color:#1c1a18;text-align:center;line-height:44px;box-shadow:0 1px 3px rgba(0,0,0,.25)}

.service{position:absolute;top:375px;width:355px;height:309px;border:2px solid var(--card-border);border-radius:8px;background:#fff;box-shadow:0 10px 10px -8px rgba(0,0,0,.2)}
.service-photo{margin:8px 8px 0;height:127px;border-radius:4px;border:1px solid #444}
.service h2{font-family:"Rokkitt",serif;font-weight:700;font-size:28px;color:var(--ink);margin:13px 0 0 13px}
.service hr{border:none;border-top:1px dotted var(--rule);margin:6px 12px 12px}
.service ul{list-style:none;margin-left:20px}
.service li{position:relative;padding-left:18px;font-size:16px;line-height:19px;margin-bottom:8px;color:#222}
.service li::before{content:"";position:absolute;left:0;top:5px;border-left:6px solid #b7872d;border-top:4px solid transparent;border-bottom:4px solid transparent}

.section-title{position:absolute;left:20px;width:1117px;font-family:"Rokkitt",serif;font-weight:700;font-size:28px;color:var(--ink);border-bottom:1px dotted var(--rule);padding-bottom:4px}
.section-title em{font-style:normal;color:var(--gold)}
.section-text{position:absolute;left:20px;font-family:Arial,Helvetica,sans-serif;font-size:13px;line-height:20px;color:var(--grey-text)}

.works-thumb{position:absolute;top:904px;width:134px;height:107px;border:1px solid #d49a3a}
.slider{position:absolute;left:503px;top:1031px}

.footer{position:absolute;left:0;top:1099px;width:1169px;height:101px;background:var(--black);border-top:3px solid var(--gold-line);color:var(--footer-yellow);font-size:16px;line-height:20px}
.footer-contact{position:absolute;left:20px;top:27px}
.footer-copy{position:absolute;right:34px;top:52px}
</style>
</head>
<body>

<header class="topbar">
  <div class="topbar-name">KORA<span>PLASTERING</span></div>
  <nav class="main-nav">
    <a href="#">About Us</a><a href="#">Our Work</a><a href="#">Testimonial</a><a href="#">Contact Us</a>
  </nav>
</header>

<section class="hero">
  <div class="hero-name">KORA<span>PLASTERING</span></div>
  <h1 class="hero-headline">WE ARE A COMPLETE SOLUTION FOR<br>YOUR HOME PLASTERING...</h1>
  <div class="hero-cta">CONTACT US</div>
</section>

<article class="service" style="left:22px">
  <div class="service-photo" role="img" aria-label="Plasterer smoothing an interior wall" style="background:linear-gradient(90deg,#6b4a2c,#a77a4e 40%,#c8894e 60%,#5a4634)"></div>
  <h2>Plastering</h2><hr>
  <ul>
    <li>Solid plastering, including hard plaster, stucco, white set.</li>
    <li>Mouldings</li>
    <li>Plasterboard</li>
  </ul>
</article>

<article class="service" style="left:401px">
  <div class="service-photo" role="img" aria-label="Trowel applying cement render" style="background:linear-gradient(90deg,#2e2e2e,#8a8a8a 45%,#b5b5b5 60%,#3a4a6a)"></div>
  <h2>Rendering</h2><hr>
  <ul>
    <li>Cement render</li>
    <li>Acrylic render</li>
    <li>Specialised coatings</li>
  </ul>
</article>

<article class="service" style="left:780px">
  <div class="service-photo" role="img" aria-label="Bedroom interior with finished cornices" style="background:linear-gradient(180deg,#e9dcc4,#c98a4a 55%,#f2ede4 75%,#3a1e24)"></div>
  <h2>Cornicing</h2><hr>
  <ul>
    <li>Custom &amp; off the shelf cornices</li>
    <li>Ornamental roses</li>
  </ul>
</article>

<h2 class="section-title" style="top:712px">Welcome To <em>Kora Plastering, Melbourne</em></h2>
<p class="section-text" style="top:766px;width:1100px">We are specialists in all aspects of plastering, rendering and cornicing throughout Melbourne. We undertake residential and commercial projects of all sizes, including home renovations, new builds and specialised architectural projects.</p>

<h2 class="section-title" style="top:848px">Our <em>Works</em></h2>
<p class="section-text" style="top:902px;width:460px">We work inside and out and take pride in delivering a high quality finish across a diversity of traditional and modern styles. We're always happy to provide advice and ideas - and deliver a service that's prompt, neat and on budget.</p>

<div class="works-thumb" style="left:527px;background:linear-gradient(135deg,#f7d46a,#e8a828 60%,#f5e7b0)" role="img" aria-label="Warm yellow living room"></div>
<div class="works-thumb" style="left:676px;background:linear-gradient(135deg,#c9643a,#d8784a 50%,#b85430)" role="img" aria-label="Textured terracotta render"></div>
<div class="works-thumb" style="left:826px;background:linear-gradient(180deg,#e8dcc0,#f4efe4 55%,#c7b79a)" role="img" aria-label="Bathroom with plastered walls"></div>
<div class="works-thumb" style="left:976px;background:linear-gradient(90deg,#6a4a2a,#e2c48e 50%,#a67c4c)" role="img" aria-label="Hallway and bathroom interior"></div>

<svg class="slider" width="634" height="40" viewBox="0 0 634 40" aria-label="Works slider">
  <defs>
    <linearGradient id="track" x1="0" y1="0" x2="0" y2="1"><stop offset="0" stop-color="#9a9484"/><stop offset=".5" stop-color="#6e6858"/><stop offset="1" stop-color="#8a8474"/></linearGradient>
    <linearGradient id="knob" x1="0" y1="0" x2="0" y2="1"><stop offset="0" stop-color="#f4f2e6"/><stop offset=".6" stop-color="#c9c6b0"/><stop offset="1" stop-color="#8e8a72"/></linearGradient>
  </defs>
  <rect x="0" y="0" width="634" height="40" rx="20" fill="#55524a"/>
  <rect x="30" y="3" width="574" height="34" rx="17" fill="url(#track)"/>
  <rect x="130" y="3" width="96" height="34" rx="17" fill="url(#knob)"/>
  <path d="M22 12 L14 20 L22 28" stroke="#111" stroke-width="3" fill="none"/>
  <path d="M612 12 L620 20 L612 28" stroke="#111" stroke-width="3" fill="none"/>
</svg>

<footer class="footer">
  <div class="footer-contact">Kora Plastering | Tel: 0400 318 562<br>&nbsp;Email: hello@koraplastering-example.com</div>
  <div class="footer-copy">© 2011, All Rights Reserved</div>
</footer>

</body>
</html>
```